washable paper bags and accessories

We are three sisters who have discovered a mutual love of bags made from washable paper. It is a brand new business venture for bags, handbags, cosmetic bags, and home storage solutions and décor all made with washable paper.
We would like to have white crumpled paper as a background for both sides. Front of card with the words "wild plum folk" only in "bohemian typewriter regular" font. Back of card with appointment style format for our next pop up stall
Target Market(s)
mums, females
Industry/Entity Type
Business
Contact Information for Business Card
ph: 0491285364
email:wildplumfolk@postnestmail.net

```html
<!DOCTYPE html>
<html lang="en">
<head>
<meta charset="UTF-8">
<title>wild plum folk – business card back</title>
<link rel="stylesheet" href="https://fonts.googleapis.com/css2?family=Special+Elite&family=Cutive+Mono&display=block">
<style>
  :root {
    --canvas: #ffffff;
    --paper-base: #dbe8e0;
    --paper-light: #eef4ef;
    --paper-highlight: #f4f8f4;
    --paper-shade: #c6dad0;
    --paper-deep: #b9d0c5;
    --ink: #141414;
  }
  * { margin: 0; padding: 0; box-sizing: border-box; }
  html, body {
    width: 1200px;
    height: 1200px;
    overflow: hidden;
    background: var(--canvas);
  }
  .canvas {
    position: relative;
    width: 1200px;
    height: 1200px;
  }
  .card {
    position: absolute;
    left: 38px;
    top: 301px;
    width: 1124px;
    height: 600px;
    overflow: hidden;
    background: var(--paper-base);
  }
  .card__paper {
    position: absolute;
    inset: 0;
    background:
      radial-gradient(ellipse 180px 90px at 12% 18%, var(--paper-highlight) 0%, transparent 70%),
      radial-gradient(ellipse 220px 110px at 38% 12%, var(--paper-shade) 0%, transparent 70%),
      radial-gradient(ellipse 200px 100px at 64% 22%, var(--paper-highlight) 0%, transparent 70%),
      radial-gradient(ellipse 240px 120px at 88% 14%, var(--paper-shade) 0%, transparent 70%),
      radial-gradient(ellipse 210px 110px at 22% 46%, var(--paper-shade) 0%, transparent 70%),
      radial-gradient(ellipse 250px 120px at 52% 44%, var(--paper-highlight) 0%, transparent 70%),
      radial-gradient(ellipse 200px 100px at 80% 50%, var(--paper-deep) 0%, transparent 70%),
      radial-gradient(ellipse 230px 110px at 10% 78%, var(--paper-light) 0%, transparent 70%),
      radial-gradient(ellipse 220px 110px at 42% 82%, var(--paper-shade) 0%, transparent 70%),
      radial-gradient(ellipse 260px 120px at 72% 80%, var(--paper-highlight) 0%, transparent 70%),
      radial-gradient(ellipse 200px 100px at 95% 88%, var(--paper-shade) 0%, transparent 70%),
      linear-gradient(160deg, var(--paper-light) 0%, var(--paper-base) 45%, var(--paper-light) 100%);
  }
  .card__headline {
    position: absolute;
    left: 0;
    right: 0;
    top: 283px;
    padding-left: 18px;
    text-align: center;
    font-family: "Special Elite", "American Typewriter", "Courier New", monospace;
    font-size: 52px;
    line-height: 60px;
    color: var(--ink);
    letter-spacing: 1px;
  }
  .card__contact {
    position: absolute;
    left: 84px;
    top: 489px;
    list-style: none;
    font-family: "Cutive Mono", "American Typewriter", "Courier New", monospace;
    font-size: 31px;
    line-height: 38px;
    color: var(--ink);
  }
</style>
</head>
<body>
  <main class="canvas">
    <section class="card">
      <div class="card__paper" role="img" aria-label="Pale mint crumpled paper texture"></div>
      <p class="card__headline">pop up stall SOON!</p>
      <ul class="card__contact">
        <li>ph: 0491285364</li>
        <li>email:wildplumfolk@postnestmail.net</li>
      </ul>
    </section>
  </main>
</body>
</html>
```